PPT Template for a company that develops software and intellectual property for use by accountants a

We are a boutique firm that develops specialised reporting applications, financial and non-financial reporting content, checklists and other intellectual property for use by business consultants and accounting firms in particular. The applications and content we are creating is strategically focussed and we are required to produce reports and presentations and our current templates are simply not sufficient.

Excel worksheets, graphs and other graphics are regularly embedded into the presentations
We have our logo in 4 colour palettes and will require the winning version to be provided in all 4 colours plus B&W. There is one single logo but the name “Lantern Trade Pathfinders” is presented in 3 different styles for use depending on the space available etc.
Our clients will typically take our products and rebrand/co brand these (we require them to at least say that there product is “powered by Lantern Trade Pathfinders” with the logo.
The templates you provide will be used to create marketing presentations, proposal presentations and our standard documents that clients will rebrand or cobrand under license.

A Powerpoint Document Slide Template

Cover page layout, back page, intermediate page heading, in colours and styles based on the logo, title styles, and an intermediate or chapter heading slide style. Many of our presentations contain slides with tables, diagrams, flowcharts and text, including simple lists of bullet points. As above, you will see in our style guide that we have four coloured logos – we would like one version in each. We recommend that we finalise the design using the maroon version and then this be used as the base for the other colour palettes.
Again, the cover should be bold and draw attention but remain professional.

We are looking for something that works in both 4:3 and 16:9 (or two templates please)

We like a clear professional and simple look.

Deliverable: PowerPoint template file (.potx extension) for PowerPoint 2007 with at least a “cover” layout, a “title and content” layout, and a simplified slide layout, as well as “back cover”. Please embed any fonts used.

Industry/Entity Type

Financial

```html
<!DOCTYPE html>
<html lang="en">
<head>
<meta charset="utf-8">
<title>Project Title Here</title>
<link href="https://fonts.googleapis.com/css2?family=Ubuntu:wght@400;500;700&display=swap" rel="stylesheet">
<style>
  :root {
    --orange: #f47320;
    --orange-light: #ff9d5c;
    --grey-light: #bdbdbd;
    --grey-mid: #7f7f7f;
    --grey-dark: #555555;
    --text: #333333;
    --white: #ffffff;
  }
  * { margin: 0; padding: 0; box-sizing: border-box; }
  html, body { width: 1200px; height: 900px; overflow: hidden; background: var(--white); }
  body { font-family: "Ubuntu", sans-serif; color: var(--text); }
  .slide { position: relative; width: 1200px; height: 900px; overflow: hidden; background: var(--white); }
  .header-accent { position: absolute; left: 0; top: 0; width: 22px; height: 85px; background: var(--orange); }
  .slide-title {
    position: absolute; left: 55px; top: 28px;
    font-size: 38px; font-weight: 500; color: var(--orange); letter-spacing: 0.5px;
  }
  .brand-name {
    position: absolute; right: 33px; top: 22px; width: 150px; text-align: right;
    font-size: 20px; font-weight: 500; line-height: 1.15; color: var(--orange);
  }
  .content { position: absolute; left: 55px; top: 245px; width: 537px; }
  .subtitle { font-size: 25px; font-weight: 700; color: var(--orange); margin-bottom: 12px; }
  .body-text { font-size: 20.5px; line-height: 36px; text-align: justify; margin-bottom: 36px; }
  .pie-chart { position: absolute; left: 682px; top: 302px; width: 470px; height: 470px; }
  .pie-label { font-family: "Ubuntu", sans-serif; font-size: 17px; font-weight: 500; text-anchor: middle; }
  .pie-label.dark { fill: #222; }
  .pie-label.light { fill: var(--white); }
  .footer {
    position: absolute; left: 0; bottom: 0; width: 1200px; height: 50px; background: var(--orange);
    display: flex; justify-content: space-between; align-items: center; padding: 0 14px;
    color: var(--white); font-size: 18px;
  }
</style>
</head>
<body>
<div class="slide">
  <div class="header-accent"></div>
  <h1 class="slide-title">PROJECT TITLE HERE</h1>
  <div class="brand-name">Lantern Trade Pathfinders</div>

  <section class="content">
    <h2 class="subtitle">PARAGRAPH SUB TITLE</h2>
    <p class="body-text">Lorem ipsum dolor sit ipsum Lorem ipsum dolor sit ipsum Lorem ipsum Lorem ipsum dolor sit ipsum Lorem ipsum dolor sit ipsum Lorem ipsum Lorem ipsum dolor sit ipsum Lorem ipsum dolor sit ipsum</p>
    <p class="body-text">Lorem ipsum Lorem ipsum dolor sit ipsum Lorem ipsum dolor sit ipsum Lorem ipsum</p>
    <p class="body-text">Lorem ipsum dolor sit ipsum Lorem ipsum dolor sit ipsum Lorem ipsum Lorem ipsum dolor sit ipsum Lorem ipsum dolor sit ipsum Lorem ipsum Lorem ipsum dolor sit ipsum Lorem ipsum dolor sit ipsum Lorem ipsum</p>
  </section>

  <svg class="pie-chart" viewBox="-235 -235 470 470" role="img" aria-label="Pie chart with five segments">
    <g stroke="#ffffff" stroke-width="2" stroke-linejoin="round">
      <path d="M0 0 L0 -230 A230 230 0 0 1 135.2 -186.1 Z" fill="var(--grey-light)"/>
      <path d="M0 0 L135.2 -186.1 A230 230 0 0 1 218.7 71.1 Z" fill="var(--orange)"/>
      <path d="M0 0 L218.7 71.1 A230 230 0 0 1 -217.5 74.9 Z" fill="var(--orange-light)"/>
      <path d="M0 0 L-217.5 74.9 A230 230 0 0 1 -128.6 -190.7 Z" fill="var(--grey-dark)"/>
      <path d="M0 0 L-128.6 -190.7 A230 230 0 0 1 0 -230 Z" fill="var(--grey-mid)"/>
    </g>
    <text class="pie-label dark" x="47" y="-167"><tspan x="47">Lorem</tspan><tspan x="47" dy="22">ipsum</tspan><tspan x="47" dy="22">dolor</tspan></text>
    <text class="pie-label light" x="-44" y="-167"><tspan x="-44">Lorem</tspan><tspan x="-44" dy="22">ipsum</tspan><tspan x="-44" dy="22">dolor</tspan></text>
    <text class="pie-label dark" x="138" y="-28"><tspan x="138">Lorem ipsum</tspan><tspan x="138" dy="23">dolor</tspan></text>
    <text class="pie-label light" x="-128" y="-35"><tspan x="-128">Lorem ipsum dolor</tspan><tspan x="-128" dy="23">Lorem ipsum dolor</tspan></text>
    <text class="pie-label dark" x="5" y="113"><tspan x="5">Lorem ipsum dolor</tspan><tspan x="5" dy="23">Lorem ipsum dolor</tspan></text>
    <circle cx="0" cy="0" r="36" fill="#ffffff" stroke="var(--orange)" stroke-width="5"/>
  </svg>

  <footer class="footer">
    <span class="copyright">Copyright text here</span>
    <span class="page-number">Page : 01</span>
  </footer>
</div>
</body>
</html>
```